Craft Beer Needs a Label/ Logo Design

Name: Tidewell
(Tidewell Ale, Tidewell Pilsner, Tidewell Stout)

We are looking for a logo-ed label that will resonate domestically and internationally for this new Craft Beer Brand.

Reason: Reviewing final and different versions submitted (edited)

Target Market(s)

Millenials

Logo Text

Tidewell Pilsner

Logo styles of interest
Emblem Logo
Character Logo
Colors

Designer to choose colors to be used in the design.

Requirements
Must have
• A labled logo design -- "Tidewell" is the name, but would like to see samples with "Ale", "Pilsner", or "Stout" after!

```html
<!DOCTYPE html>
<html lang="en">
<head>
<meta charset="utf-8">
<title>Tidewell Pilsner – Label Variants</title>
<link rel="stylesheet" href="https://fonts.googleapis.com/css2?family=Cinzel:wght@400;700&family=Fira+Sans:wght@700;800&family=Marcellus&display=swap">
<style>
  :root {
    --navy: #0c2d48;
    --outline: #0b2740;
    --frame: #7d9fbb;
    --frame-light: #93b2cb;
    --white: #ffffff;
    --gold: #f2c063;
    --sky: #c9dff3;
    --badge-fill: #5a84a8;
  }
  html, body {
    margin: 0;
    width: 1200px;
    height: 848px;
    overflow: hidden;
    background: #ffffff;
  }
  .canvas {
    position: relative;
    width: 1200px;
    height: 848px;
  }
  .label {
    position: absolute;
    top: 100px;
    width: 470px;
    height: 610px;
  }
  .label--gold { left: 95px; --accent: var(--gold); --fine-print: var(--gold); }
  .label--sky  { left: 632px; --accent: var(--sky); --fine-print: var(--sky); }

  .label__frame { fill: var(--frame); stroke: var(--outline); stroke-width: 3.5; }
  .label__frame-inner { fill: none; stroke: var(--frame-light); stroke-width: 2; }
  .label__panel { fill: var(--navy); }
  .label__badge-ring { fill: var(--navy); stroke: var(--accent); stroke-width: 5; }
  .label__badge-edge { fill: none; stroke: var(--outline); stroke-width: 3; }
  .label__badge-art { fill: var(--badge-fill); }
  .ribbon__band { fill: var(--accent); stroke: var(--outline); stroke-width: 3; }
  .ribbon__fold { fill: var(--navy); stroke: var(--outline); stroke-width: 2; }

  .brand-name {
    font-family: "Cinzel", serif;
    font-size: 44px;
    fill: var(--white);
    letter-spacing: 1px;
  }
  .brand-sub {
    font-family: "Fira Sans", sans-serif;
    font-weight: 700;
    font-size: 19px;
    fill: var(--accent);
  }
  .spec {
    font-family: "Marcellus", serif;
    font-size: 16px;
    fill: var(--white);
  }
  .beer-style {
    font-family: "Fira Sans", sans-serif;
    font-weight: 800;
    font-size: 86px;
    fill: var(--navy);
    letter-spacing: 2px;
  }
  .beer-type {
    font-family: "Cinzel", serif;
    font-size: 30px;
    fill: var(--white);
  }
  .origin {
    font-family: "Cinzel", serif;
    font-weight: 700;
    font-size: 12.5px;
    fill: var(--fine-print);
  }
</style>
</head>
<body>
<main class="canvas">

  <svg class="label label--gold" viewBox="95 100 470 610" aria-label="Tidewell Pilsner label, gold variant">
    <defs>
      <radialGradient id="glow-gold" cx="328" cy="420" r="220" gradientUnits="userSpaceOnUse">
        <stop offset="0" stop-color="#5f89ad" stop-opacity="0.75"/>
        <stop offset="0.6" stop-color="#1f4766" stop-opacity="0.35"/>
        <stop offset="1" stop-color="#0c2d48" stop-opacity="0"/>
      </radialGradient>
    </defs>
    <path class="label__frame" d="M115,200 Q115,185 130,182 L328,135 L526,182 Q541,185 541,200 L541,630 Q541,645 526,650 L328,700 L130,650 Q115,645 115,630 Z"/>
    <path class="label__frame-inner" d="M124,204 Q124,192 136,190 L328,145 L520,190 Q532,192 532,204 L532,626 Q532,638 520,642 L328,690 L136,642 Q124,638 124,626 Z"/>
    <path class="label__panel" d="M133,255 Q133,240 148,237 L328,200 L508,237 Q523,240 523,255 L523,575 Q523,590 508,594 L328,640 L148,594 Q133,590 133,575 Z"/>
    <rect x="133" y="300" width="390" height="120" fill="url(#glow-gold)" role="img" aria-label="Sunrise glow rising behind the beer style"/>
    <circle class="label__badge-edge" cx="328" cy="165" r="58"/>
    <circle class="label__badge-ring" cx="328" cy="165" r="55"/>
    <circle class="label__badge-art" cx="328" cy="165" r="45" role="img" aria-label="Brand badge emblem"/>
    <text class="brand-name" x="328" y="276" text-anchor="middle">TIDEWELL</text>
    <text class="brand-sub" x="328" y="304" text-anchor="middle">CRAFT BEERS</text>
    <text class="spec" x="185" y="412" text-anchor="middle">355mL</text>
    <text class="spec" x="470" y="412" text-anchor="middle">ALC 3.7% Vol</text>
    <path class="ribbon__fold" d="M541,418 L541,408 Q541,402 548,405 L556,410 L556,418 Z"/>
    <path class="ribbon__fold" d="M103,536 L103,548 Q103,554 110,551 L117,546 L117,536 Z"/>
    <rect class="ribbon__band" x="103" y="418" width="453" height="118"/>
    <text class="beer-style" x="328" y="511" text-anchor="middle">PILSNER</text>
    <text class="beer-type" x="328" y="584" text-anchor="middle">PREMIUM LAGER</text>
    <text class="origin" x="328" y="609" text-anchor="middle">BOTTLED IN ARIZONA, USA</text>
  </svg>

  <svg class="label label--sky" viewBox="95 100 470 610" aria-label="Tidewell Pilsner label, sky blue variant">
    <defs>
      <radialGradient id="glow-sky" cx="328" cy="420" r="220" gradientUnits="userSpaceOnUse">
        <stop offset="0" stop-color="#5f89ad" stop-opacity="0.75"/>
        <stop offset="0.6" stop-color="#1f4766" stop-opacity="0.35"/>
        <stop offset="1" stop-color="#0c2d48" stop-opacity="0"/>
      </radialGradient>
    </defs>
    <path class="label__frame" d="M115,200 Q115,185 130,182 L328,135 L526,182 Q541,185 541,200 L541,630 Q541,645 526,650 L328,700 L130,650 Q115,645 115,630 Z"/>
    <path class="label__frame-inner" d="M124,204 Q124,192 136,190 L328,145 L520,190 Q532,192 532,204 L532,626 Q532,638 520,642 L328,690 L136,642 Q124,638 124,626 Z"/>
    <path class="label__panel" d="M133,255 Q133,240 148,237 L328,200 L508,237 Q523,240 523,255 L523,575 Q523,590 508,594 L328,640 L148,594 Q133,590 133,575 Z"/>
    <rect x="133" y="300" width="390" height="120" fill="url(#glow-sky)" role="img" aria-label="Sunrise glow rising behind the beer style"/>
    <circle class="label__badge-edge" cx="328" cy="165" r="58"/>
    <circle class="label__badge-ring" cx="328" cy="165" r="55"/>
    <circle class="label__badge-art" cx="328" cy="165" r="45" role="img" aria-label="Brand badge emblem"/>
    <text class="brand-name" x="328" y="276" text-anchor="middle">TIDEWELL</text>
    <text class="brand-sub" x="328" y="304" text-anchor="middle">CRAFT BEERS</text>
    <text class="spec" x="185" y="412" text-anchor="middle">355mL</text>
    <text class="spec" x="470" y="412" text-anchor="middle">ALC 3.7% Vol</text>
    <path class="ribbon__fold" d="M541,418 L541,408 Q541,402 548,405 L556,410 L556,418 Z"/>
    <path class="ribbon__fold" d="M103,536 L103,548 Q103,554 110,551 L117,546 L117,536 Z"/>
    <rect class="ribbon__band" x="103" y="418" width="453" height="118"/>
    <text class="beer-style" x="328" y="511" text-anchor="middle">PILSNER</text>
    <text class="beer-type" x="328" y="584" text-anchor="middle">PREMIUM LAGER</text>
    <text class="origin" x="328" y="609" text-anchor="middle">BOTTLED IN ARIZONA, USA</text>
  </svg>

</main>
</body>
</html>
```